Business Card Design

We need a business card designed to the point of print ready to take to our printers. the design should be professional, easy to read and simple. The cards should represent our business as professional and trust worthy.

Attached are several versions o the logo, and also the details for the card to be printed. please do communicate if different versions of the logo is required.

Business

```html
<!DOCTYPE html>
<html lang="en">
<head>
<meta charset="utf-8">
<title>SettleMyFunds Pty Ltd – Business Card</title>
<link rel="stylesheet" href="https://fonts.googleapis.com/css2?family=Roboto+Condensed:wght@400;700&family=Roboto:wght@700&display=swap">
<style>
  :root {
    --page: #ffffff;
    --stage: #1e1d19;
    --card: #ffffff;
    --brand-orange: #f39a17;
    --brand-grey: #6f6f6f;
    --ink: #2b2622;
    --ink-soft: #5a5652;
  }
  * { margin: 0; padding: 0; box-sizing: border-box; }
  html, body {
    width: 1200px;
    height: 1000px;
    overflow: hidden;
    background: var(--page);
  }
  .stage {
    position: absolute;
    left: 18px; top: 18px;
    width: 1164px; height: 964px;
    background: var(--stage);
  }
  .card {
    position: absolute;
    left: 98px; top: 176px;
    width: 1004px; height: 649px;
    background: var(--card);
    font-family: "Roboto Condensed", sans-serif;
    color: var(--ink);
  }
  .brand-name {
    position: absolute;
    left: 70px; top: 66px;
    font-size: 62px;
    font-weight: 700;
    line-height: 1;
    color: var(--brand-grey);
    letter-spacing: -0.5px;
    white-space: nowrap;
  }
  .holder {
    position: absolute;
    left: 63px; top: 212px;
  }
  .holder-name {
    font-size: 31px;
    line-height: 1;
    letter-spacing: -0.3px;
  }
  .holder-name strong { font-weight: 700; }
  .holder-role {
    margin-top: 6px;
    font-size: 22px;
    color: var(--ink-soft);
  }
  .contact-band {
    position: absolute;
    left: 52px; top: 367px;
    width: 900px; height: 213px;
    background: var(--brand-orange);
    padding: 24px 0 0 33px;
  }
  .contact-line {
    font-size: 27px;
    line-height: 40.5px;
    white-space: nowrap;
  }
  .contact-label {
    display: inline-block;
    width: 46px;
    font-family: "Roboto", sans-serif;
    font-weight: 700;
    font-size: 24px;
  }
  .contact-label .colon {
    font-family: "Roboto Condensed", sans-serif;
    font-weight: 400;
    margin-left: 8px;
  }
  .speed-lines {
    position: absolute;
    left: 60px; top: 584px;
  }
</style>
</head>
<body>
  <div class="stage"></div>
  <section class="card">
    <div class="brand-name">SettleMyFunds Pty Ltd</div>

    <div class="holder">
      <div class="holder-name">Reid<strong>Calloway</strong></div>
      <div class="holder-role">Director</div>
    </div>

    <div class="contact-band">
      <div class="contact-line">PO Box 7260 Harbour Plaza Qld 4219</div>
      <div class="contact-line"><span class="contact-label">p<span class="colon">:</span></span>+61 400 555 174</div>
      <div class="contact-line"><span class="contact-label">e<span class="colon">:</span></span>rcalloway@settlemyfunds.com.au</div>
      <div class="contact-line"><span class="contact-label">w<span class="colon">:</span></span>www.settlemyfunds.com.au</div>
    </div>

    <svg class="speed-lines" width="892" height="24" viewBox="0 0 892 24" aria-hidden="true">
      <polygon points="0,5 892,3 892,9 0,6" fill="var(--brand-orange)"/>
      <polygon points="40,15 892,12 892,20 40,16" fill="var(--brand-orange)"/>
    </svg>
  </section>
</body>
</html>
```